Lorvane Botanic- New and unique line of Pet Products

Hi,

Lorvane Botanic is a manufacturer of natural products.

We need fresh and creative labels, for our new pet care product line:
- Specially scented for male- dog shampoo called "Pippin"
- Specially scented for female- dog shampoo called "Velvet furry"
- Cat cleaning wipes
- Stain and odor remover (for pet urine)

For more info on the products:
Lorvanebotanic.com
(please don't rely on the current labels for the pet products)

ATTACHED- you will find 2 products from Stallmart, which we like the design, as an example.

Best wishes,
Oren
Lorvane Botanicâ„¢

Reason: I did a vote, No one is very excited about the current designs Im not sure what to do next

Target Market(s)

Designed for pet owners and pet grooming professionals.

Industry/Entity Type

Pet Care

Requirements
Must have
• - The label should have a common language between products; same them, that can be modified to all products by change of writing and picture.
• - Reflects the natural aspect of the company & products, safe for the children and pets, was NOT tested on animals
• - Unique feature of the product (one destined for male dogs, other for female, the third for cats)
• Attached company Logo (Lorvane Botanicâ„¢); should appear on the label.
• - Emphasize the difference for male / female dogs.
Nice to have
• - Maybe cartoon of a family bathing the male dog / female dog / cat - ?
• I think that the common feature should be a cartoon of a pet owner/s with different pets
• Made in the USA
• - Bottles are white
• - Dimensions:
• Male dog / Female dog / Odor & stain - 6"x7" & 4.25"x11"
• Cat: 4.5"x2.5" front & back
Should not have
• Please don't use stock images;
• We do private label and cannot have similar photos as our customers, must be unique.

```html
<!DOCTYPE html>
<html lang="en">
<head>
<meta charset="utf-8">
<title>Lorvane Botanic – Pippin Oatmeal Pet Shampoo Label</title>
<link rel="stylesheet" href="https://fonts.googleapis.com/css2?family=Open+Sans:wght@400;600;700;800&family=Baloo+2:wght@800&family=Saira+Semi+Condensed:wght@700&display=swap">
<style>
  :root {
    --navy: #173f8c;
    --royal: #1a66d9;
    --sky: #3f86e3;
    --ice: #d8e9f7;
    --leaf: #a9dc86;
    --leaf-light: #e4f3d8;
    --brand-green: #6cbf3f;
    --photo-gold: #c9954e;
    --photo-grass: #6f8a3a;
    --art-blue: #5fb6f2;
    --pill-text: #cfe6ff;
    --white: #ffffff;
  }
  * { margin: 0; padding: 0; box-sizing: border-box; }
  html, body { width: 798px; height: 1200px; overflow: hidden; background: var(--white); }
  .label {
    position: relative;
    width: 798px;
    height: 1200px;
    overflow: hidden;
    font-family: "Open Sans", sans-serif;
    color: var(--navy);
  }
  .label-art { position: absolute; inset: 0; }
  .brand {
    position: absolute;
    top: 40px;
    left: 0;
    width: 100%;
    display: flex;
    justify-content: center;
    align-items: center;
    gap: 14px;
  }
  .brand-dot { width: 30px; height: 30px; border-radius: 50%; background: var(--brand-green); }
  .brand-name { font-size: 44px; font-weight: 400; color: var(--brand-green); letter-spacing: 0.5px; }
  .product-name {
    position: absolute;
    top: 518px;
    left: 0;
    width: 740px;
    text-align: center;
    font-family: "Baloo 2", sans-serif;
    font-weight: 800;
    font-size: 128px;
    line-height: 1;
    color: var(--ice);
  }
  .scent-pill {
    position: absolute;
    top: 666px;
    left: 95px;
    width: 596px;
    height: 40px;
    border-radius: 20px;
    background: var(--navy);
    color: var(--pill-text);
    font-weight: 800;
    font-size: 22px;
    letter-spacing: 0.8px;
    display: flex;
    align-items: center;
    justify-content: center;
  }
  .headline {
    position: absolute;
    top: 742px;
    left: 0;
    width: 100%;
    text-align: center;
    font-family: "Saira Semi Condensed", sans-serif;
    font-weight: 700;
    font-size: 70px;
    line-height: 74px;
    color: var(--navy);
    letter-spacing: 1px;
  }
  .benefits {
    position: absolute;
    top: 920px;
    left: 0;
    width: 100%;
    text-align: center;
    font-weight: 700;
    font-size: 24px;
    line-height: 32px;
  }
  .ingredients {
    position: absolute;
    top: 1018px;
    left: 0;
    width: 100%;
    text-align: center;
    font-size: 26px;
    letter-spacing: 0.5px;
  }
  .net-contents {
    position: absolute;
    top: 1118px;
    left: 0;
    width: 100%;
    text-align: center;
    font-weight: 700;
    font-size: 24px;
  }
</style>
</head>
<body>
<div class="label">
  <svg class="label-art" width="798" height="1200" viewBox="0 0 798 1200">
    <defs>
      <linearGradient id="side-blue" x1="0" y1="0" x2="0" y2="1">
        <stop offset="0" stop-color="#2f74dc"/>
        <stop offset="0.55" stop-color="#6fa6e8"/>
        <stop offset="1" stop-color="#e2eefa"/>
      </linearGradient>
      <linearGradient id="leaf-field" x1="1" y1="0" x2="0" y2="1">
        <stop offset="0" stop-color="#ffffff"/>
        <stop offset="0.35" stop-color="#d7efc4"/>
        <stop offset="1" stop-color="#a6d97f"/>
      </linearGradient>
      <linearGradient id="panel-fill" x1="0" y1="0" x2="0" y2="1">
        <stop offset="0" stop-color="#3a82e6"/>
        <stop offset="1" stop-color="#2f6fd6"/>
      </linearGradient>
    </defs>

    <!-- backdrop bands -->
    <path class="side-band" d="M0 0 H120 Q60 140 75 420 Q100 900 400 1200 H0 Z" fill="url(#side-blue)"/>
    <path class="leaf-band" d="M798 330 Q520 560 330 1200 H798 Z" fill="url(#leaf-field)"/>
    <rect class="base-band" x="0" y="1168" width="798" height="32" fill="var(--navy)"/>

    <!-- hero panel -->
    <path class="panel-frame" d="M18 190 Q390 128 748 150 L772 690 Q720 700 700 640 L100 640 Q40 620 30 560 Z" fill="var(--navy)"/>
    <path class="panel-face" d="M42 200 Q390 145 730 168 L746 660 Q712 660 700 620 L100 620 Q62 605 54 555 Z" fill="url(#panel-fill)"/>
    <path class="panel-inner" d="M62 212 Q390 160 712 182 L724 600 L80 600 Z" fill="var(--sky)"/>

    <rect x="71" y="176" width="186" height="133" fill="var(--photo-gold)" role="img" aria-label="Photo of a smiling golden retriever"/>
    <rect x="71" y="328" width="186" height="138" fill="var(--photo-grass)" role="img" aria-label="Photo of a rough collie lying in the grass"/>
    <path d="M300 150 Q480 100 650 170 Q720 260 700 380 Q700 500 620 510 L300 510 Q260 440 300 300 Z" fill="var(--art-blue)" role="img" aria-label="Blue stylised illustration of a puppy resting its paws on the name banner"/>

    <!-- name banner -->
    <ellipse cx="400" cy="592" rx="356" ry="80" fill="var(--navy)"/>
    <ellipse cx="396" cy="588" rx="344" ry="72" fill="var(--royal)" stroke="var(--white)" stroke-width="4"/>

    <!-- paw icon -->
    <g class="paw-icon" fill="var(--ice)">
      <ellipse cx="660" cy="598" rx="26" ry="21"/>
      <ellipse cx="626" cy="572" rx="10" ry="13"/>
      <ellipse cx="648" cy="556" rx="10" ry="13"/>
      <ellipse cx="674" cy="556" rx="10" ry="13"/>
      <ellipse cx="695" cy="574" rx="10" ry="13"/>
    </g>
  </svg>

  <div class="brand">
    <span class="brand-dot"></span>
    <span class="brand-name">Lorvane Botanic</span>
  </div>

  <div class="product-name">Pippin</div>
  <div class="scent-pill">SPECIALLY SCENTED FOR MALE DOGS</div>

  <h1 class="headline">OATMEAL<br>PET SHAMPOO</h1>

  <p class="benefits">Deodorizing, PH Balanced, Pure and Natural<br>Super Concentrated</p>
  <p class="ingredients">ALOE VERA • CHAMOMILE • VITAMIN E</p>
  <p class="net-contents">Net Contents 16 FL. OZ. (472 ML)</p>
</div>
</body>
</html>
```